Salon and Spa Distributor Business Card

Need a business card. We are are distributor in the salon and spa industry. We identify with natural beauty. Need a card with:
Company Name: Petal Harbor"
Title: "President & CEO"
Address
Company Phone number
email
website
Tag Line:" The Professional Salon Source"

Industry/Entity Type

Business

Contact Information for Business Card

Name: Leo Mendoza
Title: "President & CEO"
Address: 317 Birchline Ave, Westbrook, NJ 08412
Company Phone number: 800-463-5108
email: leomendoza@petalharbor-example.com
website: www.petalharbor-example.com

Requirements
Should not have
• No black backgrounds

```html
<!DOCTYPE html>
<html lang="en">
<head>
<meta charset="utf-8">
<title>Petal Harbor — Business Card</title>
<link rel="stylesheet" href="https://fonts.googleapis.com/css2?family=Questrial&display=swap">
<style>
  :root {
    --stage: #000000;
    --card-white: #ffffff;
    --brand-green: #3b9340;
    --tagline-green: #4cae3f;
    --ink: #2b2b2b;
    --icon-green: #3e8f46;
    --back-dark: #0b4a25;
    --back-mid: #1c7a3b;
    --back-light: #4f9a58;
    --on-green: #ffffff;
  }
  html, body {
    margin: 0;
    padding: 0;
    width: 1200px;
    height: 900px;
    overflow: hidden;
    background: var(--stage);
    font-family: "Questrial", "Century Gothic", sans-serif;
  }
  .stage {
    position: relative;
    width: 1200px;
    height: 900px;
  }
  .card {
    position: absolute;
    top: 271px;
    width: 457px;
    height: 281px;
    border-radius: 14px;
    overflow: hidden;
  }
  .card-front {
    left: 137px;
    background: var(--card-white);
  }
  .card-back {
    left: 626px;
    background: linear-gradient(215deg, var(--back-light) 0%, var(--back-mid) 55%, var(--back-dark) 100%);
  }
  .holder-name {
    position: absolute;
    left: 28px;
    top: 26px;
    margin: 0;
    font-size: 21px;
    font-weight: 400;
    letter-spacing: 0.5px;
    color: var(--brand-green);
  }
  .holder-title {
    position: absolute;
    left: 28px;
    top: 50px;
    margin: 0;
    font-size: 13px;
    color: var(--ink);
  }
  .brand-lockup {
    position: absolute;
    left: 232px;
    top: 63px;
    display: flex;
    align-items: center;
    gap: 8px;
  }
  .brand-dot {
    width: 14px;
    height: 14px;
    border-radius: 50%;
    background: var(--brand-green);
  }
  .brand-name {
    font-size: 21px;
    color: var(--brand-green);
  }
  .tagline {
    position: absolute;
    left: 0;
    right: 0;
    top: 150px;
    margin: 0;
    text-align: center;
    padding-left: 2px;
    font-size: 13.5px;
    letter-spacing: 0.3px;
    color: var(--tagline-green);
  }
  .contact-list {
    position: absolute;
    left: 28px;
    top: 201px;
    margin: 0;
    padding: 0;
    list-style: none;
    font-size: 13px;
    color: var(--ink);
  }
  .contact-list li {
    display: flex;
    align-items: center;
    gap: 6px;
    height: 16.5px;
  }
  .contact-icon {
    width: 10px;
    height: 10px;
    fill: var(--icon-green);
    flex: none;
  }
  .address {
    position: absolute;
    right: 28px;
    top: 201px;
    margin: 0;
    font-style: normal;
    text-align: right;
    font-size: 13px;
    line-height: 16.5px;
    color: var(--ink);
  }
  .back-brand {
    position: absolute;
    left: 0;
    right: 0;
    top: 114px;
    margin: 0;
    text-align: center;
    font-size: 41px;
    font-weight: 400;
    color: var(--on-green);
  }
</style>
</head>
<body>
<main class="stage">
  <section class="card card-front" aria-label="Business card front">
    <h1 class="holder-name">LEO MENDOZA</h1>
    <p class="holder-title">President &amp; CEO</p>

    <div class="brand-lockup">
      <span class="brand-dot"></span>
      <span class="brand-name">Petal Harbor</span>
    </div>

    <p class="tagline">THE PROFESSIONAL SALON SOURCE</p>

    <ul class="contact-list">
      <li>
        <svg class="contact-icon" viewBox="0 0 10 10" aria-hidden="true"><path d="M1 3.5C1 2 2.5 1.5 5 1.5S9 2 9 3.5L7.5 4 7 3H3L2.5 4ZM2.5 5H7.5L8.5 8.5H1.5Z"/></svg>
        800-463-5108
      </li>
      <li>
        <svg class="contact-icon" viewBox="0 0 10 10" aria-hidden="true"><path d="M1 2.5H9V8H1Z M1.3 2.8 5 5.6 8.7 2.8" stroke="#fff" stroke-width="0.8"/></svg>
        leomendoza@petalharbor-example.com
      </li>
      <li>
        <svg class="contact-icon" viewBox="0 0 10 10" aria-hidden="true"><circle cx="5" cy="5" r="4.3"/><path d="M3 3.5 5 4 4.5 6 6.5 7" stroke="#fff" stroke-width="0.9" fill="none"/></svg>
        www.petalharbor-example.com
      </li>
    </ul>

    <address class="address">317 Birchline Ave,<br>Westbrook,<br>NJ 08412</address>
  </section>

  <section class="card card-back" aria-label="Business card back">
    <p class="back-brand">Petal Harbor</p>
  </section>
</main>
</body>
</html>
```